KESTREL REFRIGERATION Business Card design

We are looking for a business card design front and back. We would like our logo only on the front with all other details on the rear.
Rear should include name, email address and two phone numbers. Similar to the attachment.
Smart and bright.
Looking for a matt finish on all of the card but the logo to be gloss and slightly proud.

Contact Information for Business Card

Name - Gavin Holloway
Director
Phone - 0867302948
0417259083
email - gavin@kestrelrefrigeration.com.au
website - kestrelrefrigeration.com.au

Font styles to use
Serif

Requirements
Must have
• Colours from our logo. icons for phone, email etc.

```html
<!DOCTYPE html>
<html lang="en">
<head>
<meta charset="utf-8">
<title>Kestrel Refrigeration Business Card</title>
<link rel="stylesheet" href="https://fonts.googleapis.com/css2?family=Open+Sans:wght@400;700;800&display=swap">
<style>
  :root {
    --lime: #a8f46f;
    --lime-deep: #9ce862;
    --lime-soft: #b6f784;
    --plum: #3e2a68;
    --paper: #ffffff;
    --backdrop: #eeeeea;
    --ink: #2b2b2b;
  }
  * { box-sizing: border-box; margin: 0; padding: 0; }
  html, body { width: 1200px; height: 900px; overflow: hidden; }
  body {
    background: var(--backdrop);
    font-family: "Open Sans", Arial, sans-serif;
    position: relative;
  }
  .card {
    position: absolute;
    left: 300px;
    width: 600px;
    height: 343px;
    overflow: hidden;
    box-shadow: 0 6px 18px rgba(0,0,0,0.18);
  }
  .card--front { top: 80px; }
  .card--back { top: 477px; background: var(--paper); }

  .front-field {
    position: absolute; inset: 0;
    background: linear-gradient(135deg, var(--lime-soft), var(--lime) 60%, var(--lime-deep));
  }
  .front-logo {
    position: absolute; inset: 0;
    display: flex; flex-direction: column; align-items: center; justify-content: center;
    color: var(--paper);
    font-weight: 800;
    text-align: center;
    line-height: 1.05;
  }
  .front-logo .logo-main { font-size: 58px; letter-spacing: 2px; }
  .front-logo .logo-sub { font-size: 22px; letter-spacing: 1px; margin-top: 6px; }

  .back-wave { position: absolute; inset: 0; width: 100%; height: 100%; }

  .holder { position: absolute; left: 50px; top: 70px; }
  .holder-name {
    color: var(--lime);
    font-weight: 700;
    font-size: 24px;
    letter-spacing: 0.5px;
    text-transform: uppercase;
  }
  .holder-role { color: var(--plum); font-size: 14px; padding-left: 10px; }

  .back-logo {
    position: absolute; right: 36px; top: 40px;
    color: var(--plum);
    font-weight: 800;
    text-align: right;
    line-height: 1.05;
  }
  .back-logo .logo-main { font-size: 40px; }
  .back-logo .logo-sub { font-size: 17px; margin-top: 4px; }

  .contacts {
    position: absolute; left: 86px; top: 150px;
    list-style: none;
    color: var(--ink);
    font-size: 15px;
    line-height: 21px;
  }
  .contacts li { display: flex; align-items: center; gap: 6px; }
  .contacts svg { width: 12px; height: 12px; flex: none; fill: var(--lime); }
</style>
</head>
<body>

<section class="card card--front" aria-label="Card front">
  <div class="front-field" role="img" aria-label="Lime green background with a faint diamond lattice pattern"></div>
  <div class="front-logo">
    <span class="logo-main">KESTREL</span>
    <span class="logo-sub">REFRIGERATION</span>
  </div>
</section>

<section class="card card--back" aria-label="Card back">
  <svg class="back-wave" viewBox="0 0 600 343" preserveAspectRatio="none" aria-hidden="true">
    <path d="M0,290 C150,318 320,262 480,178 C340,272 160,330 0,318 Z" fill="var(--plum)"/>
    <path d="M0,343 L0,324 C170,342 330,282 450,216 C510,186 560,176 600,178 L600,343 Z" fill="var(--lime)"/>
  </svg>

  <div class="holder">
    <p class="holder-name">Gavin Holloway</p>
    <p class="holder-role">Director</p>
  </div>

  <div class="back-logo">
    <div class="logo-main">KESTREL</div>
    <div class="logo-sub">REFRIGERATION</div>
  </div>

  <ul class="contacts">
    <li>
      <svg viewBox="0 0 12 12"><path d="M1,4 C1,2 3,1 6,1 C9,1 11,2 11,4 L8.5,4.5 L8,3 L4,3 L3.5,4.5 Z M2.5,6 L4,4.5 L8,4.5 L9.5,6 L9.5,11 L2.5,11 Z"/></svg>
      0867302948
    </li>
    <li>
      <svg viewBox="0 0 12 12"><path d="M1,4 C1,2 3,1 6,1 C9,1 11,2 11,4 L8.5,4.5 L8,3 L4,3 L3.5,4.5 Z M2.5,6 L4,4.5 L8,4.5 L9.5,6 L9.5,11 L2.5,11 Z"/></svg>
      0417259083
    </li>
    <li>
      <svg viewBox="0 0 12 12"><path d="M0.5,2.5 L11.5,2.5 L11.5,10 L0.5,10 Z M1.5,3.5 L6,7 L10.5,3.5" fill="var(--lime)" stroke="var(--paper)" stroke-width="0.8"/></svg>
      gavin@kestrelrefrigeration.com.au
    </li>
    <li>
      <svg viewBox="0 0 12 12"><circle cx="6" cy="6" r="5.5"/><path d="M0.5,6 H11.5 M6,0.5 C3,3.5 3,8.5 6,11.5 M6,0.5 C9,3.5 9,8.5 6,11.5" fill="none" stroke="var(--paper)" stroke-width="0.7"/></svg>
      kestrelrefrigeration.com.au
    </li>
  </ul>
</section>

</body>
</html>
```